Simple and Approachable Cover for Pet Expo Company Page

Size: 2000 x 430; looking simply for words "Tenbury HR Consulting" and email address "TenburyHRConsulting@mailvane.com." This is for a cover photo for a company profile page for the Northway Animal Fair, where I am a featured speaker on Employee Communications later this month. You can incorporate the attached photo to the left of the banner ad if you wish. The mood I wish to present is approachable, positive and simple.

Target Market(s)

small pet retail business owners

Industry/Entity Type

Pet Shop

Font styles to use
Serif
Sans Serif

Requirements
Must have
• Email address clearly defined/separated. Easy to read.
Nice to have
• I like the picture that I included; subtle pet paw background is also nice
Should not have
• No paid stock images

```html
<!DOCTYPE html>
<html lang="en">
<head>
<meta charset="utf-8">
<title>Tenbury HR Consulting – Cover</title>
<link href="https://fonts.googleapis.com/css2?family=Montserrat:wght@500;800&display=swap" rel="stylesheet">
<style>
  :root {
    --bg-blue: #5a8ff2;
    --bg-teal: #5ab3d8;
    --bg-green: #5fd28a;
    --band-cyan: #17d3f5;
    --band-blue: #4f7ff0;
    --text-white: #ffffff;
    --photo-grass: #7d8a4a;
    --photo-tree: #4f5a36;
    --photo-light: #b9b08a;
    --dog-brown: #4a2c22;
    --dog-white: #e9e4df;
  }
  html, body {
    margin: 0;
    padding: 0;
    overflow: hidden;
    width: 1200px;
    height: 258px;
  }
  .cover {
    position: relative;
    width: 1200px;
    height: 258px;
    overflow: hidden;
    background: linear-gradient(90deg, var(--bg-blue) 0%, var(--bg-blue) 40%, var(--bg-teal) 70%, var(--bg-green) 100%);
    font-family: "Montserrat", sans-serif;
    color: var(--text-white);
  }
  .cover__shapes {
    position: absolute;
    inset: 0;
  }
  .cover__title {
    position: absolute;
    left: 503px;
    top: 28px;
    margin: 0;
    font-weight: 800;
    font-size: 49px;
    line-height: 62px;
    letter-spacing: 0.2px;
    text-shadow: 2px 3px 3px rgba(0, 0, 0, 0.25);
  }
  .cover__email {
    position: absolute;
    left: 505px;
    top: 180px;
    display: flex;
    align-items: center;
    gap: 17px;
    font-weight: 500;
    font-size: 18px;
    letter-spacing: 0.2px;
  }
  .cover__email-icon {
    width: 22px;
    height: 16px;
  }
  .cover__dog {
    position: absolute;
    left: 918px;
    top: 8px;
    width: 248px;
    height: 250px;
    border-radius: 110px 110px 0 0;
    background: radial-gradient(ellipse at 50% 55%, var(--dog-white) 0%, #c9a98e 30%, var(--dog-brown) 65%);
  }
</style>
</head>
<body>
  <div class="cover">
    <svg class="cover__shapes" width="1200" height="258" viewBox="0 0 1200 258" aria-hidden="false">
      <defs>
        <linearGradient id="photoTone" x1="0" y1="0" x2="0" y2="1">
          <stop offset="0" stop-color="var(--photo-tree)"/>
          <stop offset="0.45" stop-color="var(--photo-light)"/>
          <stop offset="1" stop-color="var(--photo-grass)"/>
        </linearGradient>
      </defs>
      <path class="cover__band-blue" d="M368 0 C 430 50, 440 190, 395 258 L 0 258 L 0 0 Z" fill="var(--band-blue)"/>
      <path class="cover__band-cyan" d="M356 0 C 418 52, 426 190, 384 258 L 0 258 L 0 0 Z" fill="var(--band-cyan)"/>
      <path class="cover__photo" role="img" aria-label="Photo of the consultants seated on grass in a park with their two hound dogs"
            d="M345 0 C 405 55, 412 190, 372 258 L 0 258 L 0 0 Z" fill="url(#photoTone)"/>
    </svg>

    <h1 class="cover__title">Tenbury<br>HR Consulting</h1>

    <div class="cover__email">
      <svg class="cover__email-icon" viewBox="0 0 22 16" aria-hidden="true">
        <rect x="0" y="0" width="22" height="16" rx="2" fill="var(--text-white)"/>
        <path d="M1 1.5 L11 9 L21 1.5" fill="none" stroke="var(--bg-blue)" stroke-width="1.6"/>
      </svg>
      <span class="cover__email-text">TenburyHRConsulting@mailvane.com</span>
    </div>

    <div class="cover__dog" role="img" aria-label="Photo of a smiling brown and white shepherd dog"></div>
  </div>
</body>
</html>
```